PEAK KENNEL - business card
A way to remember us and buy our products
Professional
PEAKKENNEL - the finest pick
Lindmarkv. 24
SE-712 46 Eskilstuna
SWEDEN
info@peakkennel-demo.se
www.peakkennel-demo.se
I would like the business cards and other material to match.
It is about dogs and our show trolley.
I need something to hand out as I meet people at dog shows or otherwise.
your ideas are welcome to figure out what the backside should be.
drawing of product_logo related
LOGO in whole, van be split into two
4 berth
LOGO PDF
drawing pdf
Product today. Steel 2 berth

```html
<!DOCTYPE html>
<html lang="en">
<head>
<meta charset="utf-8">
<title>PEAK KENNEL – business card</title>
<link rel="stylesheet" href="https://fonts.googleapis.com/css2?family=Montserrat:wght@700&family=Open+Sans:wght@400;700&display=swap">
<style>
  :root {
    --brand-blue: #1d4f8a;
    --brand-orange: #f39200;
    --card-white: #ffffff;
    --page-bg: #e9e7e3;
    --text-light: #ffffff;
  }
  html, body {
    margin: 0;
    padding: 0;
    width: 1200px;
    height: 778px;
    overflow: hidden;
    background: var(--page-bg);
  }
  .business-card {
    position: absolute;
    left: 80px;
    top: 136px;
    width: 1040px;
    height: 506px;
    border-radius: 36px;
    overflow: hidden;
    background: var(--card-white);
    box-shadow: 0 2px 10px rgba(0,0,0,0.18);
    font-family: "Open Sans", Arial, sans-serif;
  }
  .card-bands {
    position: absolute;
    inset: 0;
  }
  .brand {
    position: absolute;
    left: 130px;
    top: 104px;
    display: flex;
    align-items: center;
    gap: 28px;
  }
  .brand-dot {
    width: 84px;
    height: 84px;
    border-radius: 50%;
    background: var(--brand-blue);
  }
  .brand-name {
    font-family: "Montserrat", Arial, sans-serif;
    font-weight: 700;
    font-size: 62px;
    letter-spacing: 1px;
    color: var(--brand-blue);
  }
  .person {
    position: absolute;
    right: 662px;
    top: 368px;
    text-align: right;
    color: var(--text-light);
  }
  .person-name {
    font-weight: 700;
    font-size: 31px;
    line-height: 38px;
  }
  .person-position {
    font-weight: 700;
    font-size: 21px;
    line-height: 30px;
  }
  .divider {
    position: absolute;
    left: 418px;
    top: 302px;
    width: 2px;
    height: 180px;
    background: var(--text-light);
  }
  .contact {
    position: absolute;
    left: 468px;
    top: 304px;
    color: var(--text-light);
    font-size: 21px;
    line-height: 34px;
  }
  .address { margin: 0 0 20px; }
  .contact-list { list-style: none; margin: 0; padding: 0; }
  .contact-list li { display: flex; align-items: center; gap: 12px; }
  .contact-icon { width: 16px; height: 16px; flex: none; }
</style>
</head>
<body>
  <article class="business-card">
    <svg class="card-bands" viewBox="0 0 1040 506" preserveAspectRatio="none" aria-hidden="true">
      <path d="M0 150 Q520 300 1040 150 L1040 506 L0 506 Z" fill="var(--brand-blue)"/>
      <path d="M0 146 Q520 280 1040 146 L1040 150 Q520 300 0 150 Z" fill="var(--brand-orange)"/>
    </svg>

    <div class="brand">
      <span class="brand-dot"></span>
      <span class="brand-name">PEAKKENNEL</span>
    </div>

    <div class="person">
      <div class="person-name">Your Name</div>
      <div class="person-position">Position</div>
    </div>

    <div class="divider"></div>

    <div class="contact">
      <p class="address">Lindmarkv. 24<br>SE-712 46 Eskilstuna, SWEDEN</p>
      <ul class="contact-list">
        <li>
          <svg class="contact-icon" viewBox="0 0 16 16" aria-hidden="true"><rect x="4" y="1" width="8" height="14" rx="1.5" fill="none" stroke="#fff" stroke-width="1.6"/><circle cx="8" cy="12.3" r="0.9" fill="#fff"/></svg>
          <span>+46 70 5550182</span>
        </li>
        <li>
          <svg class="contact-icon" viewBox="0 0 16 16" aria-hidden="true"><rect x="1" y="3.5" width="14" height="9" fill="none" stroke="#fff" stroke-width="1.6"/><path d="M1 3.5 L8 9 L15 3.5" fill="none" stroke="#fff" stroke-width="1.4"/></svg>
          <span>info@peakkennel-demo.se</span>
        </li>
        <li>
          <svg class="contact-icon" viewBox="0 0 16 16" aria-hidden="true"><circle cx="8" cy="8" r="6.5" fill="none" stroke="#fff" stroke-width="1.5"/><ellipse cx="8" cy="8" rx="2.8" ry="6.5" fill="none" stroke="#fff" stroke-width="1.2"/><path d="M1.5 8 H14.5" stroke="#fff" stroke-width="1.2"/></svg>
          <span>www.peakkennel-demo.se</span>
        </li>
      </ul>
    </div>
  </article>
</body>
</html>
```